We are looking for an effective ad to recruit work from home Loan Officers for our Mortgage Brokerage.
Use the following text...
Earn Mortgage Income in your sleep. Its as easy as 1, 2, 3.....
1) Solicit Potential Applicants (Word of Mouth, Email, Social Media etc.)
2) Take Complete Applications & Submit Them
3) Wait to Get Paid.......(Avg. $2,500 per closing)
"You open the door, we'll finish the deal"
No Experience Necessary
No Goals or Quotas
No Office Hours / Work from Home Office
...and We Fully Reimburse ALL LICENSING FEES!!
Email Resume to mwelby@brightharborloans.example
Bright Harbor Lending Group, Inc.
947 W Caldwell Avenue, #318
Baltimore, MD 21230
NMLS #731860
www.brightharborloans.example
Phone (800) 555-0142
Licensed Mortgage Broker in MD and DC since 1997
Target Market(s)
Professionals looking to earn part time income at Loan Officers, preferably with strong social media following.
Industry/Entity Type
Loan
Look and feel

```html
<!DOCTYPE html>
<html lang="en">
<head>
<meta charset="utf-8">
<title>Earn Mortgage Income In Your Sleep</title>
<link rel="stylesheet" href="https://fonts.googleapis.com/css2?family=Alfa+Slab+One&family=Oswald:wght@500;600&family=Open+Sans:ital,wght@0,600;0,700;1,700&display=swap">
<style>
  :root {
    --brand-blue: #1d5ba9;
    --brand-olive: #a99a36;
    --olive-dark: #8f8229;
    --paper: #ffffff;
    --swoosh-grey: #c9c9c9;
    --photo-light: #e9d9d3;
    --photo-dark: #7a5a4c;
  }
  * { margin: 0; padding: 0; box-sizing: border-box; }
  html, body { width: 969px; height: 1200px; overflow: hidden; background: var(--paper); }
  .flyer { position: relative; width: 969px; height: 1200px; overflow: hidden; background: var(--paper); font-family: "Open Sans", sans-serif; }

  .hero-photo { position: absolute; left: 470px; top: 0; width: 499px; height: 600px; background: linear-gradient(160deg, var(--photo-light) 0%, #c9a99a 45%, var(--photo-dark) 100%); }

  .headline { position: absolute; left: 44px; top: 44px; font-family: "Alfa Slab One", serif; font-weight: 400; line-height: 1; }
  .headline span { display: block; white-space: nowrap; }
  .headline .earn { color: var(--brand-blue); font-size: 120px; letter-spacing: 2px; }
  .headline .mortgage { color: var(--brand-olive); font-size: 62px; margin-top: -6px; }
  .headline .income { color: var(--brand-blue); font-size: 88px; margin-top: -3px; }
  .headline .sleep { color: var(--brand-olive); font-size: 44px; margin-top: 7px; }

  .brand-name { position: absolute; left: 52px; top: 445px; display: flex; align-items: center; gap: 12px; color: var(--brand-blue); font-weight: 700; font-size: 19px; line-height: 1.2; width: 320px; }
  .brand-name .mark { width: 40px; height: 40px; flex: none; background: var(--brand-olive); border-radius: 50%; }

  .swoosh { position: absolute; left: 0; top: 520px; width: 969px; height: 110px; }

  .olive-panel { position: absolute; left: 0; top: 600px; width: 969px; height: 490px; background: var(--brand-olive); }

  .steps { position: absolute; left: 65px; top: 628px; color: var(--paper); }
  .steps h2 { font-family: "Oswald", sans-serif; font-weight: 500; font-size: 36px; line-height: 1; letter-spacing: .5px; }
  .steps ol { list-style: none; margin-top: 14px; font-weight: 700; font-size: 24px; line-height: 33px; }
  .steps ol small { font-size: 20px; }

  .tagline-pill { position: absolute; left: 33px; top: 803px; width: 880px; height: 80px; background: var(--brand-blue); border-radius: 40px; color: var(--paper); font-family: "Oswald", sans-serif; font-weight: 500; font-size: 41px; display: flex; align-items: center; justify-content: center; letter-spacing: .5px; }

  .perks { position: absolute; left: 62px; top: 918px; list-style: none; color: var(--paper); font-weight: 700; font-size: 23px; line-height: 28px; }
  .perks li { display: flex; gap: 14px; }
  .perks .tick { width: 20px; height: 20px; flex: none; margin-top: 4px; }
  .perks .cont { padding-left: 34px; }

  .license-burst { position: absolute; left: 680px; top: 888px; width: 264px; height: 128px; }
  .license-burst svg { position: absolute; left: 0; top: 0; }
  .license-burst p { position: absolute; left: 32px; top: 32px; width: 200px; text-align: center; transform: rotate(12deg); color: var(--brand-blue); font-weight: 700; font-style: italic; font-size: 15px; line-height: 18px; }

  .social-badge { position: absolute; left: 716px; top: 1018px; width: 208px; height: 66px; background: var(--paper); border: 3px solid var(--brand-blue); border-radius: 6px; }

  .footer-rule { position: absolute; left: 0; top: 1088px; width: 969px; height: 4px; background: var(--paper); }
  .footer-rule.blue { top: 1092px; height: 5px; background: var(--brand-blue); }
  .footer-rule.olive { top: 1097px; height: 4px; background: var(--olive-dark); }

  .contact { position: absolute; left: 0; top: 1101px; width: 969px; height: 99px; background: var(--brand-blue); color: var(--paper); text-align: center; }
  .contact .email { font-weight: 700; font-size: 25px; margin-top: 10px; }
  .contact .details { font-weight: 700; font-size: 17px; line-height: 25px; margin-top: 4px; }
</style>
</head>
<body>
<main class="flyer">
  <div class="hero-photo" role="img" aria-label="Photo of a smiling woman holding a fan of hundred-dollar bills"></div>

  <h1 class="headline">
    <span class="earn">EARN</span>
    <span class="mortgage">MORTGAGE</span>
    <span class="income">INCOME</span>
    <span class="sleep">IN YOUR SLEEP.</span>
  </h1>

  <div class="brand-name"><span class="mark"></span><span>Bright Harbor Lending Group, Inc.</span></div>

  <svg class="swoosh" viewBox="0 0 969 110" preserveAspectRatio="none" aria-hidden="true">
    <path d="M0 40 C300 10 650 20 969 75 L969 110 L0 110 Z" fill="#a99a36"/>
    <path d="M0 12 C320 -8 650 0 969 62 L969 80 C650 20 320 20 0 40 Z" fill="#c9c9c9"/>
    <path d="M0 22 C320 2 650 10 969 70 L969 76 C650 18 320 12 0 32 Z" fill="#ffffff"/>
  </svg>

  <div class="olive-panel"></div>

  <section class="steps">
    <h2>ITS AS EASY AS</h2>
    <ol>
      <li>1. Solicit Potential Applicants <small>(Word of Mouth, Email, Social Media etc.)</small></li>
      <li>2. Take Complete Applications &amp; Submit Them</li>
      <li>3. Wait to Get Paid...... (Avg. $2,500 per closing)</li>
    </ol>
  </section>

  <div class="tagline-pill">"YOU OPEN THE DOOR, WE'LL FINISH THE DEAL"</div>

  <ul class="perks">
    <li><svg class="tick" viewBox="0 0 20 20" aria-hidden="true"><circle cx="10" cy="10" r="9" fill="#fff"/><path d="M5.5 10.5 L8.8 13.5 L14.5 6.8" stroke="#a99a36" stroke-width="2.6" fill="none"/></svg>No Experience Necessary</li>
    <li><svg class="tick" viewBox="0 0 20 20" aria-hidden="true"><circle cx="10" cy="10" r="9" fill="#fff"/><path d="M5.5 10.5 L8.8 13.5 L14.5 6.8" stroke="#a99a36" stroke-width="2.6" fill="none"/></svg>No Goals or Quotas</li>
    <li><svg class="tick" viewBox="0 0 20 20" aria-hidden="true"><circle cx="10" cy="10" r="9" fill="#fff"/><path d="M5.5 10.5 L8.8 13.5 L14.5 6.8" stroke="#a99a36" stroke-width="2.6" fill="none"/></svg>No Office Hours / Work from Home Office ...</li>
    <li class="cont">and We Fully Reimburse ALL LICENSING FEES!!</li>
  </ul>

  <div class="license-burst">
    <svg viewBox="0 0 264 128" width="264" height="128" aria-hidden="true">
      <polygon fill="#fff" points="14,4 64,18 92,0 120,16 160,2 182,22 236,14 230,40 262,56 238,72 258,100 212,100 200,126 160,112 124,128 100,110 52,122 52,98 4,92 28,70 0,50 30,36"/>
    </svg>
    <p>Licensed Mortgage<br>Broker in MD and<br>DC since 1997</p>
  </div>

  <div class="social-badge" aria-hidden="true"></div>

  <div class="footer-rule"></div>
  <div class="footer-rule blue"></div>
  <div class="footer-rule olive"></div>

  <footer class="contact">
    <p class="email">Email Resume to mwelby@brightharborloans.example</p>
    <p class="details">Bright Harbor Lending Group, Inc. | 947 W Caldwell Avenue, #318, Baltimore, MD 21230<br>NMLS #731860 | www.brightharborloans.example | Ph (800) 555-0142</p>
  </footer>
</main>
</body>
</html>
```